Cedar Bend Remedy Barn Label

I am looking to make a trendy and classy look for a label for our CBD products that's going on a green bottle and would like the writing on the label to be white I want a rustic farm look using different shades of green , I would like to keep it as Country Texas with the hipster flare as possible. I would like to keep it professional but look cool. I would like to incorporate the cross somewhere in there. We need room for nutriticianal facts info about the product i.e size of bottle fl , mg, and a qr code

```html
<!DOCTYPE html>
<html lang="en">
<head>
<meta charset="UTF-8">
<title>Cedar Bend Remedy Barn – CBD Label</title>
<link href="https://fonts.googleapis.com/css2?family=Jost:wght@400&family=Rokkitt:wght@700&display=swap" rel="stylesheet">
<style>
  :root {
    --page: #f4f4f4;
    --label-black: #0b0b0b;
    --label-charcoal: #2a2a2a;
    --lime: #a6d23a;
    --slate: #34495e;
    --ink: #111111;
  }
  html, body {
    margin: 0;
    padding: 0;
    width: 1200px;
    height: 1200px;
    overflow: hidden;
    background: var(--page);
  }
  .canvas {
    position: relative;
    width: 1200px;
    height: 1200px;
  }
  .label {
    position: absolute;
    left: 120px;
    top: 82px;
    width: 960px;
    height: 1036px;
    overflow: hidden;
    background: radial-gradient(ellipse 70% 60% at 62% 45%, #333333 0%, var(--label-charcoal) 30%, #161616 65%, var(--label-black) 100%);
  }
  .brand-mark {
    position: absolute;
    left: 40px;
    top: 60px;
    width: 190px;
    height: 190px;
    background: var(--slate);
  }
  .brand-name {
    position: absolute;
    left: 276px;
    top: 22px;
    margin: 0;
    font-family: "Rokkitt", serif;
    font-weight: 700;
    font-size: 112px;
    line-height: 92px;
    letter-spacing: 0;
    color: var(--lime);
    text-transform: uppercase;
    white-space: nowrap;
    transform: scaleX(0.82);
    transform-origin: left top;
  }
  .brand-tagline {
    position: absolute;
    left: 322px;
    top: 206px;
    margin: 0;
    font-family: "Rokkitt", serif;
    font-weight: 700;
    font-size: 60px;
    line-height: 60px;
    color: var(--slate);
    text-transform: uppercase;
    white-space: nowrap;
    transform: scaleX(0.82);
    transform-origin: left top;
  }
  .product-box {
    position: absolute;
    left: 277px;
    top: 357px;
    width: 397px;
    height: 255px;
    border: 4px solid var(--lime);
    text-align: center;
    font-family: "Jost", sans-serif;
    font-weight: 400;
    color: var(--lime);
  }
  .product-box .product-name {
    display: block;
    font-size: 184px;
    line-height: 1;
    margin-top: 8px;
    letter-spacing: -3px;
  }
  .product-box .product-grade {
    display: block;
    font-size: 78px;
    line-height: 1;
    margin-top: -14px;
    letter-spacing: -1px;
  }
  .spectrum-band {
    position: absolute;
    left: 0;
    top: 807px;
    width: 960px;
    height: 78px;
    background: var(--lime);
    display: flex;
    align-items: center;
    justify-content: center;
    font-family: "Jost", sans-serif;
    font-size: 60px;
    color: var(--ink);
  }
  .extract-tag {
    position: absolute;
    left: 358px;
    top: 885px;
    width: 238px;
    height: 44px;
    background: var(--lime);
    border-radius: 0 0 16px 16px;
    display: flex;
    align-items: center;
    justify-content: center;
    font-family: "Jost", sans-serif;
    font-size: 31px;
    color: var(--ink);
  }
  .volume {
    position: absolute;
    left: 0;
    top: 950px;
    width: 960px;
    text-align: center;
    font-family: "Jost", sans-serif;
    font-size: 29px;
    color: var(--lime);
  }
</style>
</head>
<body>
  <main class="canvas">
    <section class="label">
      <div class="brand-mark"></div>
      <h1 class="brand-name">Cedar Bend<br>Remedy Barn</h1>
      <p class="brand-tagline">CBD Wellness Center</p>

      <div class="product-box">
        <span class="product-name">CBD</span>
        <span class="product-grade">ORGANIC</span>
      </div>

      <div class="spectrum-band">FULL SPECTRUM</div>
      <div class="extract-tag">CO2 EXTRACT</div>
      <div class="volume">30ml</div>
    </section>
  </main>
</body>
</html>
```